Long term design collaboration - mobile app design & web app design

We are looking for a talented mobile designer to help us improve our UI & UX for mobile app and web app.

The screens that need to be redesigned are attached.

There is potentially a lot more work in future design available for the successful candidate.
The successful candidate would have to take part in daily stand-up around 3 times per week.
The successful candidate would join a dev team
We are software company that does property management

```html
<!DOCTYPE html>
<html lang="en">
<head>
<meta charset="utf-8">
<title>Corvo – Billing</title>
<link href="https://fonts.googleapis.com/css2?family=Inter:wght@400;500;600;700&display=swap" rel="stylesheet">
<style>
:root{
  --bg:#f4f4f4;
  --surface:#ffffff;
  --ink:#1d1d1f;
  --ink-soft:#3a3a3c;
  --muted:#6b6b70;
  --line:#e3e3e6;
  --brand:#2a5bbf;
  --brand-light:#4a90e8;
  --info-bg:#eef5fd;
  --info-line:#bcd6f2;
  --badge:#d9443f;
  --mint-bg:#eefaf5;
  --mint-line:#8edcc2;
  --mint:#4fbf94;
  --pill-grey:#a8a8ad;
  --pill-pale:#d9d9dc;
}
*{box-sizing:border-box;margin:0;padding:0}
html,body{width:1200px;height:873px;overflow:hidden}
body{background:var(--bg);font-family:'Inter',sans-serif;color:var(--ink);position:relative}
.sidebar,.topbar,.main{position:absolute;background:var(--surface);border-radius:12px}
.sidebar{left:27px;top:27px;width:233px;height:819px}
.brand{position:absolute;left:13px;top:16px;font-size:20px;font-weight:700;letter-spacing:-.3px}
.icon-btn{position:absolute;display:flex;align-items:center;justify-content:center;background:#fff;border:1px solid var(--line);border-radius:7px;box-shadow:0 1px 2px rgba(0,0,0,.08)}
.sidebar .close{left:189px;top:13px;width:31px;height:31px}
.section-label{position:absolute;left:13px;font-size:10px;letter-spacing:1px;color:var(--muted);font-weight:500}
.nav-item{position:absolute;left:13px;width:207px;height:34px;display:flex;align-items:center;padding-left:9px;gap:10px;font-size:14px;color:var(--ink-soft);border-radius:6px}
.nav-item svg{width:18px;height:18px;flex:none;stroke:currentColor;fill:none;stroke-width:1.6;stroke-linecap:round;stroke-linejoin:round}
.nav-item.active{background:var(--brand);color:#fff}
.nav-item .badge{position:absolute;right:7px;width:20px;height:20px;border-radius:4px;background:var(--badge);color:#fff;font-size:10px;font-weight:600;display:flex;align-items:center;justify-content:center}
.nav-item .caret{position:absolute;right:10px;width:12px;height:12px}
.logout{position:absolute;left:13px;top:778px;display:flex;align-items:center;gap:10px;font-size:14px;color:var(--ink)}
.logout svg{width:18px;height:18px;stroke:currentColor;fill:none;stroke-width:1.6}
.sidebar .expand{left:193px;top:780px;width:27px;height:27px}

.topbar{left:273px;top:27px;width:900px;height:60px}
.back{left:14px;top:13px;width:65px;height:33px;font-size:12.5px;font-weight:600;gap:5px}
.crumbs{position:absolute;left:92px;top:23px;font-size:12.5px;color:var(--muted);display:flex;gap:10px;align-items:center}
.crumbs .current{color:var(--ink);font-weight:600}
.bell{left:647px;top:13px;width:33px;height:33px}
.avatar{position:absolute;left:701px;top:13px;width:32px;height:32px;border-radius:6px;background:linear-gradient(135deg,#3b3b3d,#8a8480)}
.user{position:absolute;left:740px;top:15px}
.user .name{font-size:13.5px;font-weight:600}
.user .role{font-size:10.5px;color:var(--muted);margin-top:2px}
.user-caret{position:absolute;left:870px;top:25px}

.main{left:273px;top:100px;width:900px;height:746px}
.title{position:absolute;left:14px;top:16px;font-size:19px;font-weight:700}
.lede{position:absolute;left:14px;top:47px;font-size:12px;color:var(--muted)}
.updated{position:absolute;left:14px;top:77px;width:873px;height:43px;background:var(--info-bg);border-radius:6px;font-size:12px;padding:14px 13px;color:var(--ink)}
.rule{position:absolute;left:14px;top:139px;width:873px;height:1px;background:var(--line)}
.col-head{position:absolute;top:165px;font-size:15px;font-weight:700}
.pill{position:absolute;display:flex;align-items:center;justify-content:center;border-radius:6px;font-size:11.5px;color:#fff}
.card{position:absolute;top:200px;border:1px solid var(--line);border-radius:7px}
.balance{position:absolute;left:19px;top:19px;width:387px;height:120px;border:1px solid var(--info-line);border-radius:5px;overflow:hidden}
.balance .currency{height:33px;background:var(--info-bg);border-bottom:1px solid var(--info-line);display:flex;align-items:center;gap:7px;padding-left:12px;font-size:12px}
.flag{width:20px;height:20px;border-radius:50%;background:linear-gradient(135deg,#1f3e8c 0 45%,#d23b3b 45% 55%,#1f3e8c 55%)}
.balance .amount{position:absolute;left:13px;top:46px;font-size:30px;font-weight:700;letter-spacing:-.5px}
.balance .caption{position:absolute;left:13px;top:90px;font-size:11.5px;color:var(--muted)}
.primary-btn{position:absolute;left:19px;width:387px;height:40px;background:var(--brand);color:#fff;border-radius:5px;display:flex;align-items:center;justify-content:center;font-size:12px;font-weight:500}
.method{position:absolute;left:19px;width:388px;height:70px;border:1px solid var(--line);border-radius:5px}
.method.primary{background:var(--mint-bg);border-color:var(--mint-line)}
.method .mark{position:absolute;left:13px;top:14px;width:40px;height:40px;border-radius:50%;background:#fff;border:1px solid var(--mint-line);display:flex;align-items:center;justify-content:center;font-size:9px;font-weight:600;color:var(--ink-soft)}
.method .label{position:absolute;left:63px;top:15px;font-size:13.5px;font-weight:600}
.method .number{position:absolute;left:63px;top:40px;font-size:11.5px;color:var(--muted);letter-spacing:.3px}
.method .delete{position:absolute;top:17px;font-size:10.5px}
.method .pill{top:12px;height:20px;border-radius:10px;font-size:10.5px}
.note{position:absolute;left:19px;top:241px;font-size:11.5px;color:var(--muted)}
</style>
</head>
<body>

<aside class="sidebar">
  <div class="brand">Corvo</div>
  <div class="icon-btn close"><svg width="12" height="12" viewBox="0 0 12 12" stroke="#1d1d1f" stroke-width="1.6" stroke-linecap="round"><path d="M2 2l8 8M10 2l-8 8"/></svg></div>

  <div class="section-label" style="top:66px">OVERVIEW</div>
  <div class="nav-item" style="top:106px"><svg viewBox="0 0 24 24"><path d="M4 11l8-7 8 7v9h-5v-6H9v6H4z"/></svg>Home</div>
  <div class="nav-item" style="top:143px"><svg viewBox="0 0 24 24"><path d="M4 10v4h3l7 4V6L7 10z M18 9l2-1 M18 12h3 M18 15l2 1"/></svg>Announcements</div>
  <div class="nav-item" style="top:180px"><svg viewBox="0 0 24 24"><path d="M6 17V11a6 6 0 0112 0v6l1 1H5z M10 20h4"/></svg>Notifications<span class="badge">2</span></div>
  <div class="nav-item" style="top:216px"><svg viewBox="0 0 24 24"><rect x="3" y="6" width="18" height="13" rx="1"/><path d="M3 7l9 6 9-6"/></svg>Messages<span class="badge">9</span></div>

  <div class="section-label" style="top:256px">FINANCIAL</div>
  <div class="nav-item" style="top:286px"><svg viewBox="0 0 24 24"><path d="M3 9l9-5 9 5z M5 10v7 M10 10v7 M14 10v7 M19 10v7 M3 20h18"/></svg>Bank Balance<svg class="caret" viewBox="0 0 12 12"><path d="M3 4.5l3 3 3-3"/></svg></div>
  <div class="nav-item active" style="top:296px;top:296px"><svg viewBox="0 0 24 24"><path d="M6 3h12v18l-3-2-3 2-3-2-3 2z M9 8h6 M9 12h6 M9 16h3"/></svg>Billing</div>
  <div class="nav-item" style="top:333px;top:333px"><svg viewBox="0 0 24 24"><rect x="4" y="4" width="16" height="16" rx="1"/><path d="M8 8h1 M12 8h1 M16 8h0 M8 12h1 M12 12h1 M8 16h1 M12 16h1 M16 12h0 M16 16h0"/></svg>Ground Rent</div>
  <div class="nav-item" style="top:369px"><svg viewBox="0 0 24 24"><path d="M6 3h9l4 4v14H6z M12 9v8 M14 11h-3a1.5 1.5 0 000 3h2a1.5 1.5 0 010 3h-3"/></svg>Property Balance<svg class="caret" viewBox="0 0 12 12"><path d="M3 4.5l3 3 3-3"/></svg></div>
  <div class="nav-item" style="top:406px"><svg viewBox="0 0 24 24"><path d="M6 3h9l4 4v14H6z M9 17l6-6 M9.5 11.5h0 M14.5 16.5h0"/></svg>Service Charge</div>

  <div class="section-label" style="top:446px">MANAGEMENT &amp; RESOURCES</div>
  <div class="nav-item" style="top:476px"><svg viewBox="0 0 24 24"><rect x="4" y="4" width="16" height="16" rx="1"/><path d="M10 9l-3 3 3 3 M14 9l3 3-3 3"/></svg>Development Parameters</div>
  <div class="nav-item" style="top:513px"><svg viewBox="0 0 24 24"><ellipse cx="12" cy="6" rx="7" ry="3"/><path d="M5 6v12c0 1.7 3 3 7 3s7-1.3 7-3V6 M5 12c0 1.7 3 3 7 3s7-1.3 7-3"/></svg>Directory</div>
  <div class="nav-item" style="top:549px"><svg viewBox="0 0 24 24"><rect x="5" y="3" width="14" height="18" rx="1"/><path d="M8 8h8 M8 12h8 M8 16h5"/></svg>Documents<svg class="caret" viewBox="0 0 12 12"><path d="M3 4.5l3 3 3-3"/></svg></div>
  <div class="nav-item" style="top:586px"><svg viewBox="0 0 24 24"><path d="M12 3l8 4.5v9L12 21l-8-4.5v-9z M4 7.5l8 4.5 8-4.5 M12 12v9"/></svg>Packages</div>

  <div class="section-label" style="top:626px">SETTINGS &amp; SUPPORT</div>
  <div class="nav-item" style="top:656px"><svg viewBox="0 0 24 24"><circle cx="12" cy="12" r="3"/><path d="M12 3v3 M12 18v3 M3 12h3 M18 12h3 M5.6 5.6l2.1 2.1 M16.3 16.3l2.1 2.1 M5.6 18.4l2.1-2.1 M16.3 7.7l2.1-2.1"/></svg>Settings<svg class="caret" viewBox="0 0 12 12"><path d="M3 4.5l3 3 3-3"/></svg></div>
  <div class="nav-item" style="top:693px"><svg viewBox="0 0 24 24"><path d="M4 14a8 8 0 0116 0 M4 14v3h3v-4H4 M20 14v3h-3v-4h3 M17 17c0 2-2 3-5 3"/></svg>Tickets<span class="badge">1</span></div>

  <div class="logout"><svg viewBox="0 0 24 24"><path d="M10 4H5v16h5 M15 8l4 4-4 4 M19 12H9"/></svg>Logout</div>
  <div class="icon-btn expand"><svg width="10" height="10" viewBox="0 0 10 10" fill="none" stroke="#1d1d1f" stroke-width="1.4"><path d="M4 2l3 3-3 3"/></svg></div>
</aside>

<header class="topbar">
  <div class="icon-btn back"><svg width="14" height="14" viewBox="0 0 14 14" fill="none" stroke="#1d1d1f" stroke-width="1.6" stroke-linecap="round"><path d="M12 7H2 M6 3L2 7l4 4"/></svg>Back</div>
  <nav class="crumbs"><span>Dashboard</span><span>›</span><span>Financial</span><span>›</span><span class="current">Billing</span></nav>
  <div class="icon-btn bell"><svg width="16" height="16" viewBox="0 0 24 24" fill="none" stroke="#1d1d1f" stroke-width="1.8"><path d="M6 17V11a6 6 0 0112 0v6l1 1H5z M10 20h4"/><circle cx="17" cy="5" r="2.5" fill="#d9443f" stroke="none"/></svg></div>
  <div class="avatar" role="img" aria-label="Profile photo of the signed-in user"></div>
  <div class="user"><div class="name">Clara Whitmore</div><div class="role">Development Manager</div></div>
  <svg class="user-caret" width="12" height="12" viewBox="0 0 12 12" fill="none" stroke="#1d1d1f" stroke-width="1.6"><path d="M3 4.5l3 3 3-3"/></svg>
</header>

<main class="main">
  <h1 class="title">Finances</h1>
  <p class="lede">Provides a centralized overview of subaccounts and payment providers, enabling streamlined transaction management and real-time balance monitoring</p>
  <div class="updated">Last updated: 27 December 2024 09:37</div>
  <div class="rule"></div>

  <h2 class="col-head" style="left:14px">Subaccount</h2>
  <div class="pill" style="left:329px;top:160px;width:111px;height:27px;background:var(--pill-pale)">Not Connected</div>
  <section class="card" style="left:14px;width:427px;height:213px">
    <div class="balance">
      <div class="currency"><span class="flag"></span>Sterling (GBP)</div>
      <div class="amount">£123,456,789</div>
      <div class="caption">Your available balances</div>
    </div>
    <div class="primary-btn" style="top:153px">+ Add Subaccount</div>
  </section>

  <h2 class="col-head" style="left:460px">Payment Provider</h2>
  <div class="pill" style="left:799px;top:160px;width:88px;height:27px;background:var(--brand-light)">Connected</div>
  <section class="card" style="left:460px;width:427px;height:276px">
    <div class="method primary" style="top:19px">
      <div class="mark">OC</div>
      <div class="label">Orbit Card • GBP</div>
      <div class="number">****-****-****-2089</div>
      <div class="delete" style="left:272px">Delete</div>
      <div class="pill" style="left:316px;width:57px;background:var(--mint)">Primary</div>
    </div>
    <div class="method" style="top:102px">
      <div class="mark">Vela</div>
      <div class="label">Vela • USD</div>
      <div class="number">****-****-****-7093</div>
      <div class="delete" style="left:239px">Delete</div>
      <div class="pill" style="left:283px;width:90px;background:var(--pill-grey)">Set as Primary</div>
    </div>
    <div class="primary-btn" style="top:186px">+ Add More Payment Provider</div>
    <p class="note">You can add a credit or debit card up to 5</p>
  </section>
</main>

</body>
</html>
```